Travel Consultant Business Card

Hello.. New travel consultant looking seeking a business card that incorporates my new logo. I specialize in cruises but also want to imply land vacation. I am very open to any design and font concepts. I'm looking for a very upbeat modern design that reflects cruise and land vacations. Bright vibrant colors

Target Market(s)

Cruise and Land Vacationers

Industry/Entity Type

Travel Agent

Contact Information for Business Card

I am very open to any design and font concepts. I'm looking for a very upbeat modern design that reflects cruise and land vacations. Bright vibrant colors

Colors

Designer to choose colors to be used in the design.

Requirements
Must have
• Company Name: MapleRidge Journeys---New logo uploaded to be included in design
• My Name: Dolores Kwiatek-Travel Consultant
• Phone Number: (555) 418-7093
• E-Mail Address: mapleridgejourneys@examplemail.net
• Website: www.mapleridgejourneys.example
Nice to have
• My tag line is …..Here to Get You There

```html
<!DOCTYPE html>
<html lang="en">
<head>
<meta charset="utf-8">
<title>MapleRidge Journeys – Business Card</title>
<link href="https://fonts.googleapis.com/css2?family=Montserrat:wght@700&family=Roboto:wght@400;700&family=Yellowtail&display=swap" rel="stylesheet">
<style>
  :root {
    --stage: #2b2b2d;
    --card-white: #ffffff;
    --navy: #1d3f97;
    --royal: #1a5fb4;
    --sky: #2fa9e2;
    --pale-sky: #7fd0f5;
    --pattern-light: #e6f4fc;
    --pattern-mid: #9fd6f3;
  }
  * { box-sizing: border-box; margin: 0; padding: 0; }
  html, body { width: 1200px; height: 902px; overflow: hidden; }
  body { background: var(--stage); position: relative; font-family: "Roboto", Arial, sans-serif; }

  .card {
    position: absolute;
    width: 560px;
    height: 320px;
    border-radius: 26px;
    overflow: hidden;
    background: var(--card-white);
  }

  /* Back of card */
  .card--back { left: 70px; top: 90px; }
  .back-pattern {
    position: absolute; inset: 0;
    background: radial-gradient(ellipse at center, var(--pattern-light) 0%, var(--pattern-mid) 100%);
  }
  .back-brand {
    position: absolute; left: 0; right: 0; top: 50%;
    transform: translateY(-50%);
    text-align: center;
    font-family: "Montserrat", Arial, sans-serif;
    font-weight: 700; font-size: 34px;
    color: var(--navy);
  }

  /* Front of card */
  .card--front { left: 570px; top: 480px; }
  .waves { position: absolute; inset: 0; width: 100%; height: 100%; }

  .person { position: absolute; right: 36px; top: 26px; text-align: right; }
  .person__name { font-weight: 700; font-size: 19px; color: var(--navy); }
  .person__title { font-size: 14px; color: var(--sky); margin-top: 2px; }

  .brand { position: absolute; left: 28px; top: 80px; }
  .brand__name {
    display: flex; align-items: center; gap: 10px;
    font-family: "Montserrat", Arial, sans-serif;
    font-weight: 700; font-size: 27px; line-height: 34px; color: var(--navy);
  }
  .brand__dot { width: 14px; height: 14px; border-radius: 50%; background: var(--sky); flex: none; }
  .brand__tagline {
    font-family: "Yellowtail", "Brush Script MT", cursive;
    font-size: 28px; line-height: 34px; color: var(--navy);
    margin-top: 6px; margin-left: 24px;
  }

  .contact {
    position: absolute; right: 26px; top: 190px;
    list-style: none; text-align: right;
    color: var(--card-white); font-size: 13px; line-height: 24px;
  }
  .contact li { display: flex; justify-content: flex-end; align-items: center; gap: 8px; }
  .contact svg { width: 14px; height: 14px; flex: none; }
</style>
</head>
<body>

  <section class="card card--back">
    <div class="back-pattern" role="img" aria-label="All-over pattern of light blue travel icons: planes, palm trees, landmarks, ships' wheels, cameras and beach items"></div>
    <div class="back-brand">MapleRidge Journeys</div>
  </section>

  <section class="card card--front">
    <svg class="waves" viewBox="0 0 560 320" preserveAspectRatio="none" aria-hidden="true">
      <path d="M0,228 C100,236 200,214 282,176 C205,226 100,250 0,250 Z" fill="var(--pale-sky)"/>
      <path d="M0,258 C120,266 230,236 312,180 C245,248 120,282 0,282 Z" fill="var(--sky)"/>
      <path d="M560,55 C440,58 380,110 320,170 C250,240 160,292 0,296 L0,320 L560,320 Z" fill="var(--royal)"/>
      <path d="M150,316 C230,310 280,292 310,272 C280,300 230,314 150,316 Z" fill="var(--card-white)"/>
    </svg>

    <div class="person">
      <p class="person__name">Dolores Kwiatek</p>
      <p class="person__title">Travel Consultant</p>
    </div>

    <div class="brand">
      <p class="brand__name"><span class="brand__dot"></span>MapleRidge Journeys</p>
      <p class="brand__tagline">Here to Get You There</p>
    </div>

    <ul class="contact">
      <li>(555) 418-7093
        <svg viewBox="0 0 24 24" fill="currentColor"><path d="M6.6 10.8a15.1 15.1 0 0 0 6.6 6.6l2.2-2.2a1 1 0 0 1 1-.25 11.4 11.4 0 0 0 3.6.57 1 1 0 0 1 1 1V20a1 1 0 0 1-1 1A17 17 0 0 1 3 4a1 1 0 0 1 1-1h3.5a1 1 0 0 1 1 1c0 1.25.2 2.45.57 3.6a1 1 0 0 1-.25 1z"/></svg>
      </li>
      <li>mapleridgejourneys@examplemail.net
        <svg viewBox="0 0 24 24" fill="none" stroke="currentColor" stroke-width="2"><rect x="3" y="5" width="18" height="14" rx="1"/><path d="M3 6l9 7 9-7"/></svg>
      </li>
      <li>www.mapleridgejourneys.example
        <svg viewBox="0 0 24 24" fill="none" stroke="currentColor" stroke-width="2"><circle cx="12" cy="12" r="9"/><path d="M3 12h18M12 3c3 3 3 15 0 18M12 3c-3 3-3 15 0 18"/></svg>
      </li>
    </ul>
  </section>

</body>
</html>
```